Webdesign für lokalen Dart-Shop
Zielgruppe
Wir sind ein lokaler Dart-Shop in Hamburg, welcher in Norddeutschland sehr beliebt ist und bundesweit das Größte Angebot bietet. Durch unseren Online-Shop möchte wir unseren Radius erweitern.
Zielgruppe: Dart Anfänger, Fortgeschrittene sowie Vereine und Unternehmen
Aufgabenstellung
In jedem Fall das Haupt-Element unseres Logo´s, einer Dart-Scheibe.

```html
<!DOCTYPE html>
<html lang="de">
<head>
<meta charset="utf-8">
<title>Pfeilwerk Nord – Ladeninfo</title>
<link rel="stylesheet" href="https://fonts.googleapis.com/css2?family=Ubuntu:wght@500&family=Roboto:wght@500;700&display=swap">
<style>
  :root {
    --page-white: #ffffff;
    --text-dark: #1e1e1e;
    --footer-black: #070707;
    --footer-text: #ffffff;
    --accent-red: #c8161d;
    --photo-door: #8a5a48;
    --photo-shelf: #5d5a5c;
    --photo-bar: #c9c4c2;
  }
  * { margin: 0; padding: 0; box-sizing: border-box; }
  html, body { width: 1200px; height: 675px; overflow: hidden; background: var(--page-white); }
  .page { position: relative; width: 1200px; height: 675px; }

  .notice {
    position: absolute; top: 0; left: 0; width: 1200px; height: 300px;
    background: var(--page-white);
  }
  .notice-text {
    position: absolute; left: 165px; top: 8px; width: 820px;
    font-family: "Ubuntu", sans-serif; font-weight: 500;
    font-size: 15.5px; line-height: 23px; color: var(--text-dark);
  }
  .notice-text p + p { margin-top: 23px; }

  .shop-photos { position: absolute; top: 160px; left: 183px; display: flex; gap: 40px; }
  .shop-photo { width: 254px; height: 118px; }
  .photo-entrance { background: linear-gradient(90deg, #d8d6d4 0%, var(--photo-door) 45%, #5a6f8a 100%); }
  .photo-boards { background: linear-gradient(135deg, #2c2c30 0%, var(--photo-shelf) 50%, #a33a3c 100%); }
  .photo-coffee { background: linear-gradient(180deg, #7a5c5a 0%, var(--photo-bar) 55%, #3a3a3a 100%); }

  .site-footer {
    position: absolute; top: 300px; left: 0; width: 1200px; height: 375px;
    background: var(--footer-black); color: var(--footer-text);
    font-family: "Roboto", sans-serif;
  }
  .footer-col { position: absolute; top: 14px; }
  .col-more { left: 212px; }
  .col-contact { left: 594px; }
  .footer-heading { font-size: 16px; font-weight: 500; margin-bottom: 6px; letter-spacing: 0.2px; }
  .footer-list { list-style: none; font-size: 13px; font-weight: 700; line-height: 23px; }
  .hours-heading { margin-top: 23px; font-size: 13px; font-weight: 700; line-height: 23px; }

  .directions { position: absolute; left: 212px; top: 235px; }
  .directions .footer-heading { margin-bottom: 4px; }
  .address { font-size: 13px; font-weight: 500; line-height: 23px; color: var(--accent-red); font-style: normal; }
  .parking { font-size: 13px; font-weight: 700; line-height: 23px; width: 720px; }

  .to-top { position: absolute; right: 32px; bottom: 4px; }
</style>
</head>
<body>
<div class="page">
  <section class="notice">
    <div class="notice-text">
      <p>Alle wartenden Kunden können auf unseren Bänken vor dem Pfeilwerk Platz nehmen und bekommen von uns gratis Kaffee oder Soft-Getränke!<br>Bitte achtet auch hier auf den Mindestabstand!</p>
      <p>Danke für Euer Verständnis und bleibt gesund. #dartswm #darts</p>
    </div>
    <div class="shop-photos">
      <div class="shop-photo photo-entrance" role="img" aria-label="Foto des Ladeneingangs mit Backsteinfassade und Schaufenster"></div>
      <div class="shop-photo photo-boards" role="img" aria-label="Foto der Verkaufsfläche mit Dartscheiben und Regalen"></div>
      <div class="shop-photo photo-coffee" role="img" aria-label="Foto der Kaffeetheke im Laden"></div>
    </div>
  </section>

  <footer class="site-footer">
    <div class="footer-col col-more">
      <h2 class="footer-heading">MEHR ÜBER</h2>
      <ul class="footer-list">
        <li>Impressum</li>
        <li>Kontakt</li>
        <li>Versand- &amp; Zahlungsbedingungen</li>
        <li>Widerrufsrecht &amp; Muster-Widerrufsformular</li>
        <li>AGB</li>
        <li>Privatsphäre und Datenschutz</li>
        <li>Callback Service</li>
      </ul>
    </div>
    <div class="footer-col col-contact">
      <h2 class="footer-heading">KONTAKT</h2>
      <ul class="footer-list">
        <li>Tel: 040 555 018 42 - 0</li>
        <li>Fax: 040 555 018 42 - 9</li>
        <li>hallo@pfeilwerk-nord.de</li>
        <li>www.pfeilwerk-nord.de</li>
      </ul>
      <h3 class="hours-heading">SHOP ÖFFNUNGSZEITEN</h3>
      <p class="footer-list">Montag - Samstag 12:00 - 18:00</p>
    </div>
    <div class="directions">
      <h2 class="footer-heading">ANFAHRT</h2>
      <address class="address">Pfeilwerk Nord GmbH<br>Lindenweg 14<br>20099 Hamburg</address>
      <p class="parking">Parkmöglichkeiten direkt vor dem Ladengeschäft oder in der Einbahnstraße, welche direkt um das Grundstück herum führt. S-Bahn Lindenplatz nur 300m entfernt!</p>
    </div>
    <svg class="to-top" width="28" height="20" viewBox="0 0 28 20" aria-hidden="true">
      <path d="M2 20 A12 12 0 0 1 26 20 Z" fill="#1c1c1c"/>
      <path d="M9 16 L14 11 L19 16" fill="none" stroke="#ffffff" stroke-width="2"/>
    </svg>
  </footer>
</div>
</body>
</html>
```